Blood bank stickers for dog and cat blood donors

We’d like to create two promotional stickers to give to clients after their pet donates blood at TORLO. These will help raise awareness and celebrate our donor pets.

One for dogs: “My dog is a blood donor hero at TORLO”
One for cats: “My cat is a blood donor hero at TORLO”

It'll need to include:

1. TORLO Blood Bank

2. Address: Unit 3/218 Karrinup Drive, Wendale, 6172

2. Phone: (08) 9387 2614

3. TORLO logo (attached)

Something people would proudly display on their car or laptop.

Target Market(s)

Pet owner community

Industry/Entity Type

Veterinary

Colors
0054AA
0677BA
7BADD7
CADEEF
E8F1F8
0094D4
00A9DD
6FCCEA
C7EBF8
E9F6FB
EB3D1F
EC4F4E
F09395
F8D3D4
FCEDEE

Requirements
Must have
• "TORLO Blood Bank" & "Unit 3/218 Karrinup Drive, Wendale, 6172" & "(08) 9387 2614"
Nice to have
• Maybe a tag line like "My Dog is a Blood Donor Hero" & "My Cat is a Blood Donor Hero"

```html
<!DOCTYPE html>
<html lang="en">
<head>
<meta charset="utf-8">
<title>TORLO Blood Bank Donor Stickers</title>
<link rel="stylesheet" href="https://fonts.googleapis.com/css2?family=Lato:wght@700;900&display=swap">
<style>
  :root {
    --page: #ffffff;
    --rim: #0d4a6e;
    --band: #45a3b0;
    --field: #eaf5fa;
    --heading: #0d4a6e;
    --ink: #1e1e1e;
    --wordmark: #111111;
  }
  html, body {
    margin: 0;
    padding: 0;
    width: 1200px;
    height: 1000px;
    overflow: hidden;
    background: var(--page);
  }
  .sticker-sheet {
    position: relative;
    width: 1200px;
    height: 1000px;
  }
  .sticker {
    position: absolute;
    left: 362px;
    width: 440px;
    height: 440px;
  }
  .sticker--dog { top: 42px; }
  .sticker--cat { top: 522px; }
  .sticker-rim { fill: var(--rim); }
  .sticker-band { fill: var(--band); }
  .sticker-field { fill: var(--field); }
  .logo-dot { fill: var(--band); }
  .arc-tagline {
    font-family: "Lato", sans-serif;
    font-weight: 900;
    font-size: 21px;
    letter-spacing: 0.3px;
    fill: var(--heading);
    text-transform: uppercase;
  }
  .wordmark {
    font-family: "Lato", sans-serif;
    font-weight: 900;
    font-size: 34px;
    fill: var(--wordmark);
  }
  .bank-name {
    font-family: "Lato", sans-serif;
    font-weight: 700;
    font-size: 17px;
    fill: var(--heading);
  }
  .contact-line {
    font-family: "Lato", sans-serif;
    font-weight: 700;
    font-size: 18px;
    fill: var(--ink);
  }
</style>
</head>
<body>
<main class="sticker-sheet">
  <svg width="0" height="0" style="position:absolute" aria-hidden="true">
    <defs>
      <path id="tagline-arc" d="M -110.7,71.9 A 132 132 0 1 1 110.7,71.9"/>
      <g id="scallop-field">
        <circle r="172"/>
        <circle cx="178" cy="0" r="20" transform="rotate(0)"/>
        <circle cx="178" cy="0" r="20" transform="rotate(18)"/>
        <circle cx="178" cy="0" r="20" transform="rotate(36)"/>
        <circle cx="178" cy="0" r="20" transform="rotate(54)"/>
        <circle cx="178" cy="0" r="20" transform="rotate(72)"/>
        <circle cx="178" cy="0" r="20" transform="rotate(90)"/>
        <circle cx="178" cy="0" r="20" transform="rotate(108)"/>
        <circle cx="178" cy="0" r="20" transform="rotate(126)"/>
        <circle cx="178" cy="0" r="20" transform="rotate(144)"/>
        <circle cx="178" cy="0" r="20" transform="rotate(162)"/>
        <circle cx="178" cy="0" r="20" transform="rotate(180)"/>
        <circle cx="178" cy="0" r="20" transform="rotate(198)"/>
        <circle cx="178" cy="0" r="20" transform="rotate(216)"/>
        <circle cx="178" cy="0" r="20" transform="rotate(234)"/>
        <circle cx="178" cy="0" r="20" transform="rotate(252)"/>
        <circle cx="178" cy="0" r="20" transform="rotate(270)"/>
        <circle cx="178" cy="0" r="20" transform="rotate(288)"/>
        <circle cx="178" cy="0" r="20" transform="rotate(306)"/>
        <circle cx="178" cy="0" r="20" transform="rotate(324)"/>
        <circle cx="178" cy="0" r="20" transform="rotate(342)"/>
      </g>
    </defs>
  </svg>

  <svg class="sticker sticker--dog" viewBox="-220 -220 440 440" aria-label="Dog donor sticker">
    <circle class="sticker-rim" r="218"/>
    <circle class="sticker-band" r="208"/>
    <use class="sticker-field" href="#scallop-field"/>
    <text class="arc-tagline"><textPath href="#tagline-arc" startOffset="50%" text-anchor="middle">My dog is a blood donor hero at TORLO</textPath></text>
    <circle class="logo-dot" cx="0" cy="-48" r="26"/>
    <text class="wordmark" x="0" y="16" text-anchor="middle">torlo</text>
    <text class="bank-name" x="0" y="64" text-anchor="middle">TORLO Blood Bank</text>
    <text class="contact-line" x="0" y="93" text-anchor="middle">Unit 3/218 Karrinup Drive,</text>
    <text class="contact-line" x="0" y="115" text-anchor="middle">Wendale, 6172</text>
    <text class="contact-line" x="0" y="145" text-anchor="middle">(08) 9387 2614</text>
  </svg>

  <svg class="sticker sticker--cat" viewBox="-220 -220 440 440" aria-label="Cat donor sticker">
    <circle class="sticker-rim" r="218"/>
    <circle class="sticker-band" r="208"/>
    <use class="sticker-field" href="#scallop-field"/>
    <text class="arc-tagline"><textPath href="#tagline-arc" startOffset="50%" text-anchor="middle">My cat is a blood donor hero at TORLO</textPath></text>
    <circle class="logo-dot" cx="0" cy="-48" r="26"/>
    <text class="wordmark" x="0" y="16" text-anchor="middle">torlo</text>
    <text class="bank-name" x="0" y="64" text-anchor="middle">TORLO Blood Bank</text>
    <text class="contact-line" x="0" y="93" text-anchor="middle">Unit 3/218 Karrinup Drive,</text>
    <text class="contact-line" x="0" y="115" text-anchor="middle">Wendale, 6172</text>
    <text class="contact-line" x="0" y="145" text-anchor="middle">(08) 9387 2614</text>
  </svg>
</main>
</body>
</html>
```